Minimalist, Flat(Matte) design for a Beef Jerky packaging company. No bullshit company looking for a

Need a packaging design for a new Beef Jerky product(in English). The name of the company is 'Velmor' and thus the packaging should reflect the bullish, tough, and simple nature of the beef jerky product. The finished product should communicate simplicity, minimalism, yet toughness and strength.

The logo should be simple, with a minimal number of colors , and should be either all white/cream, or have some red as well. Main colors should be white, cream, tinted red, and matte black. I think 4 colors max would be best. The closest example to an existing package style would be Korvanti Dusk clove cigarettes( image attached).

It will be on a matte black standing pouch package. See image for package type. Package dimensions:

Dimension: Width x Gusset x Height
INCH : 5.125" (W) x 3.125" (G) x 8.125" (H)
MILLIMETER : 130mm (W) x 80mm (G) x 205mm (H)

I don't have anything totally specific so artistic liberty is encouraged, provided the colors are kept to a minimum and looks consistent with the simple nature of the brand and the matte black packaging.

Also attached an existing beef jerky package with a similar style to what we're looking for.

Industry/Entity Type

It Company

Colors
f59195
ffffff

Requirements
Must have
• Low contrast, flat and minimalist design.
Should not have
• A complicated design with many colors. Gawdy/flashy design. Bright colors. High contrast.

```html
<!DOCTYPE html>
<html lang="en">
<head>
<meta charset="utf-8">
<title>Velmor Peppered Beef Jerky – Pouch Front and Back</title>
<link href="https://fonts.googleapis.com/css2?family=Cormorant+Garamond:wght@500&family=Dancing+Script:wght@500&family=Raleway:wght@400;500;600&family=Saira+Condensed:wght@400&display=swap" rel="stylesheet">
<style>
  :root {
    --pouch-black: #0b0b0b;
    --blush: #f59195;
    --white: #ffffff;
    --zip-grey: #2a2a2a;
    --page: #ffffff;
  }
  * { margin: 0; padding: 0; box-sizing: border-box; }
  html, body {
    width: 1200px;
    height: 895px;
    overflow: hidden;
    background: var(--page);
  }
  .canvas {
    position: relative;
    width: 1200px;
    height: 895px;
  }
  .pouch {
    position: absolute;
    top: 91px;
    width: 400px;
    height: 632px;
  }
  .pouch--front { left: 172px; }
  .pouch--back { left: 610px; }
  .pouch__shape {
    position: absolute;
    inset: 0;
    width: 400px;
    height: 632px;
  }
  .pouch__text {
    position: absolute;
    left: 0;
    right: 0;
    text-align: center;
    line-height: 1;
  }
  .open-here {
    position: absolute;
    top: 23px;
    font-family: "Raleway", sans-serif;
    font-size: 6px;
    font-weight: 600;
    letter-spacing: 0.4px;
    color: var(--white);
  }
  .pouch--front .open-here { left: 12px; }
  .pouch--back .open-here { right: 12px; }
  .brand-name {
    font-family: "Saira Condensed", sans-serif;
    font-weight: 400;
    color: var(--white);
    letter-spacing: 1px;
  }
  .pouch--front .brand-name { top: 129px; font-size: 34px; }
  .pouch--back .brand-name { top: 345px; font-size: 31px; }
  .tagline-script {
    top: 276px;
    font-family: "Dancing Script", cursive;
    font-size: 26px;
    color: var(--blush);
  }
  .flavour {
    top: 313px;
    font-family: "Cormorant Garamond", serif;
    font-weight: 500;
    font-size: 60px;
    color: var(--white);
    letter-spacing: 0.5px;
  }
  .product-type {
    top: 384px;
    font-family: "Raleway", sans-serif;
    font-weight: 500;
    font-size: 19px;
    letter-spacing: 0.8px;
    color: var(--blush);
  }
  .net-weight {
    top: 564px;
    font-family: "Raleway", sans-serif;
    font-weight: 600;
    font-size: 14px;
    color: var(--white);
  }
  .pouch--back .net-weight {
    color: var(--blush);
    font-size: 13px;
  }
  .back-tagline {
    top: 391px;
    font-family: "Raleway", sans-serif;
    font-weight: 600;
    font-size: 9.5px;
    line-height: 14px;
    letter-spacing: 0.3px;
    color: var(--blush);
  }
  .back-copy {
    top: 433px;
    left: 112px;
    right: 112px;
    font-family: "Raleway", sans-serif;
    font-weight: 400;
    font-size: 9.4px;
    line-height: 12.8px;
    color: var(--white);
  }
</style>
</head>
<body>
<main class="canvas">

  <section class="pouch pouch--front" aria-label="Pouch front">
    <svg class="pouch__shape" viewBox="0 0 400 632" aria-hidden="true">
      <path d="M6,0 H394 Q400,0 400,6 V18 L395,23 L400,28 L390,632 H10 L0,28 L5,23 L0,18 V6 Q0,0 6,0 Z" fill="var(--pouch-black)"/>
      <rect x="12" y="48" width="376" height="6" rx="3" fill="var(--zip-grey)"/>
      <circle cx="200" cy="104" r="15" fill="var(--white)"/>
      <path d="M101.4,312 A102,102 0 0 1 298.6,312" fill="none" stroke="var(--white)" stroke-width="2.4"/>
      <path d="M105,372 A102,102 0 0 0 156,427" fill="none" stroke="var(--white)" stroke-width="2.4"/>
      <path d="M295,372 A102,102 0 0 1 244,427" fill="none" stroke="var(--white)" stroke-width="2.4"/>
      <polygon points="123,427 277,427 200,512" fill="var(--blush)"/>
      <line x1="121" y1="554" x2="121" y2="590" stroke="var(--white)" stroke-width="1.2"/>
      <line x1="284" y1="554" x2="284" y2="590" stroke="var(--white)" stroke-width="1.2"/>
    </svg>
    <svg class="pouch__shape" viewBox="0 0 400 632">
      <rect x="4" y="182" width="392" height="6" fill="var(--blush)" role="img" aria-label="Blush zigzag trim band across the pouch"/>
    </svg>
    <span class="open-here">OPEN HERE</span>
    <p class="pouch__text brand-name">VELMOR</p>
    <p class="pouch__text tagline-script">Hand crafted</p>
    <h1 class="pouch__text flavour">PEPPERED</h1>
    <p class="pouch__text product-type">BEEF JERKY</p>
    <p class="pouch__text net-weight">NET WT: 3 oz / 100g ℮</p>
  </section>

  <section class="pouch pouch--back" aria-label="Pouch back">
    <svg class="pouch__shape" viewBox="0 0 400 632" aria-hidden="true">
      <path d="M6,0 H394 Q400,0 400,6 V18 L395,23 L400,28 L390,632 H10 L0,28 L5,23 L0,18 V6 Q0,0 6,0 Z" fill="var(--pouch-black)"/>
      <rect x="12" y="48" width="376" height="6" rx="3" fill="var(--zip-grey)"/>
      <circle cx="200" cy="322" r="14" fill="var(--white)"/>
    </svg>
    <svg class="pouch__shape" viewBox="0 0 400 632">
      <rect x="4" y="182" width="392" height="6" fill="var(--blush)" role="img" aria-label="Blush zigzag trim band across the pouch"/>
    </svg>
    <span class="open-here">OPEN HERE</span>
    <p class="pouch__text brand-name">VELMOR</p>
    <p class="pouch__text back-tagline">HAND CRAFTED<br>BEEF JERKY</p>
    <p class="pouch__text back-copy">Lorem ipsum dolor sit amet, consectetuer adipiscing elit, sed diam nonummy nibh euismod tincidunt ut laoreet dolore magna aliquam erat volutpat. Ut wisi enim ad minim veniam, quis nostrud exerci tation ullamcorper suscipit lobortis nisl ut aliquip ex ea commodo consequat.</p>
    <p class="pouch__text net-weight">NET WT: 3 oz / 100g ℮</p>
  </section>

</main>
</body>
</html>
```